Laundromat washing machine soap instructions poster

I own a laundromat and need a poster explaining to my customers how to load the soap, bleach and fabric softener into our washing machines. I tried to make a poster on canva but it looks terrible. My Laundromat is called "Suds Harbor" and would like my logo to also be on the poster for branding. I would like the poster to use my blue logo colors to match my brand identity.
Under the photo please include the following text:
" *Please place pods inside the washer"
Thanks
Laundromat

```html
<!DOCTYPE html>
<html lang="en">
<head>
<meta charset="utf-8">
<title>Suds Harbor – Soap Loading Poster</title>
<link rel="stylesheet" href="https://fonts.googleapis.com/css2?family=Montserrat:wght@600;700;800&display=swap">
<style>
  :root{
    --stage:#d1d2d4;
    --paper:#ffffff;
    --brand-deep:#1f6fb2;
    --brand-mid:#2386c8;
    --brand-light:#22a3da;
    --machine-grey:#8e9092;
    --machine-pale:#e4e4e0;
  }
  *{box-sizing:border-box;margin:0;padding:0}
  html,body{width:1200px;height:1200px;overflow:hidden;background:var(--stage)}
  body{font-family:"Montserrat",sans-serif;position:relative}
  .poster{position:absolute;left:204px;top:40px;width:792px;height:1120px;background:var(--paper);overflow:hidden}
  .poster-art,.pointers{position:absolute;inset:0}
  .pointers{pointer-events:none}
  .brand{position:absolute;left:56px;top:92px;display:flex;align-items:center;gap:10px;
    color:var(--brand-mid);font-weight:800;font-size:27px;letter-spacing:.3px;text-transform:uppercase;white-space:nowrap}
  .brand-dot{width:18px;height:18px;border-radius:50%;background:var(--brand-mid)}
  .headline{position:absolute;left:0;right:0;top:266px;text-align:center;
    color:var(--brand-deep);font-weight:700;font-size:24px}
  .dispenser-photo{position:absolute;left:208px;top:310px;width:369px;height:558px;border-radius:10px;
    background:linear-gradient(180deg,var(--machine-grey) 0%,#a5a7a8 45%,var(--machine-pale) 62%,var(--machine-grey) 100%)}
  .label{position:absolute;height:25px;padding:0 8px;border-radius:8px;background:var(--brand-deep);
    color:#fff;font-weight:700;font-size:18px;line-height:25px;text-align:center;white-space:nowrap}
  .label--softener{left:54px;top:566px;width:166px}
  .label--bleach{left:619px;top:566px;width:117px}
  .label--detergent-left{left:54px;top:684px;width:116px}
  .label--detergent-right{left:619px;top:682px;width:119px}
  .pods-note{position:absolute;left:74px;top:875px;width:649px;height:54px;border-radius:18px;background:#fff;
    color:var(--brand-deep);font-weight:700;font-size:29px;line-height:54px;text-align:center}
</style>
</head>
<body>
<main class="poster">
  <svg class="poster-art" width="792" height="1120" viewBox="0 0 792 1120">
    <defs>
      <linearGradient id="band" x1="0" y1="1" x2="1" y2="0">
        <stop offset="0" stop-color="#1f6fb2"/>
        <stop offset="1" stop-color="#22a3da"/>
      </linearGradient>
      <linearGradient id="bubbleTop" x1="1" y1="0" x2="0" y2="1">
        <stop offset="0" stop-color="#3d9fe0"/>
        <stop offset="1" stop-color="#e6f4fc"/>
      </linearGradient>
      <linearGradient id="bubbleBottom" x1="0" y1="0" x2="0" y2="1">
        <stop offset="0" stop-color="#ffffff"/>
        <stop offset=".35" stop-color="#a9d7f3"/>
        <stop offset="1" stop-color="#2d8fd8"/>
      </linearGradient>
    </defs>
    <path role="img" aria-label="Water bubbles decoration" d="M545,0 L792,0 L792,250 L380,250 C460,180 510,100 545,0 Z" fill="url(#bubbleTop)"/>
    <rect role="img" aria-label="Water bubbles decoration" x="0" y="740" width="792" height="380" fill="url(#bubbleBottom)"/>
    <path class="swoosh" d="M0,308 C230,300 450,200 560,0 L470,0 C360,170 180,235 0,243 Z" fill="url(#band)"/>
    <path d="M0,260 C200,250 380,180 470,0 L545,0 C440,190 230,255 0,265 Z" fill="#22a3da"/>
  </svg>

  <div class="brand"><span class="brand-dot"></span>Suds Harbor</div>
  <h1 class="headline">Where dose the soap go?</h1>
  <div class="dispenser-photo" role="img" aria-label="Photo of the washer's open soap dispenser drawer with four compartments"></div>

  <svg class="pointers" width="792" height="1120" viewBox="0 0 792 1120" aria-hidden="true">
    <defs>
      <marker id="arrowHead" viewBox="0 0 10 10" refX="6" refY="5" markerWidth="4" markerHeight="4" orient="auto">
        <path d="M0,0 L10,5 L0,10 Z" fill="#2386c8"/>
      </marker>
    </defs>
    <g fill="none" stroke="#2386c8" stroke-width="5" stroke-linecap="round" marker-end="url(#arrowHead)">
      <path d="M222,592 C265,584 298,598 314,628"/>
      <path d="M625,596 C570,580 498,586 462,616"/>
      <path d="M172,704 C228,680 290,690 310,724"/>
      <path d="M625,706 C570,690 505,694 482,714"/>
    </g>
    <g fill="none" stroke="#2386c8" stroke-width="1.6">
      <path d="M145,620 C185,608 215,602 250,600"/>
      <path d="M165,628 C195,620 220,616 240,614"/>
      <path d="M560,604 C600,606 630,612 640,618"/>
      <path d="M585,612 C610,614 628,618 636,622"/>
      <path d="M135,722 C175,712 205,706 240,704"/>
      <path d="M150,730 C180,724 205,720 225,718"/>
      <path d="M570,712 C605,714 630,716 650,712"/>
    </g>
  </svg>

  <span class="label label--softener">Fabric Softener</span>
  <span class="label label--bleach">Bleach</span>
  <span class="label label--detergent-left">Detergent</span>
  <span class="label label--detergent-right">Detergent</span>

  <p class="pods-note">Please place pods inside the washer</p>
</main>
</body>
</html>
```